Fertility Book Cover

This is a book about infertility, treatment options and solutions. The book title is "Nos caminhos do berço". The book is in portuguese, but I believe that won't be a problem to design the cover. I need front and back covers design.
The author name, that should be in book is "Dra. Marta Quevedo Bonfanti Rocha".

Letter case could be "Nos Caminhos do Berço"

This is the cover I created, but I don't like it: http://www.plivora.com/doc/583019472/20957318-cover

8.5" x 11"

Target Market(s)

Woman and Couples that desire kids and have problem about fertility

Colors
b768aa
e34196
6b449a

Requirements
Nice to have
• a link to our domain: www.ninhovivo.org (not essential)
More happy images than sad woman...

```html
<!DOCTYPE html>
<html lang="pt">
<head>
<meta charset="utf-8">
<title>Nos caminhos do berço</title>
<link href="https://fonts.googleapis.com/css2?family=Just+Another+Hand&display=swap" rel="stylesheet">
<style>
  :root {
    --page: #ffffff;
    --cover-pink: #e24296;
    --ink-purple: #6b449a;
    --soft-lilac: #b768aa;
    --white: #ffffff;
  }
  html, body {
    margin: 0;
    padding: 0;
    width: 1200px;
    height: 1000px;
    overflow: hidden;
    background: var(--page);
  }
  .canvas {
    position: relative;
    width: 1200px;
    height: 1000px;
  }
  .book-cover {
    position: absolute;
    left: 294px;
    top: 100px;
    width: 612px;
    height: 792px;
    background: var(--cover-pink);
  }
  .cover-art {
    position: absolute;
    left: 0;
    top: 0;
    font-family: "Just Another Hand", "Arial Narrow", sans-serif;
  }
  .author {
    fill: var(--ink-purple);
    font-size: 34px;
  }
  .title-word {
    fill: var(--white);
    font-size: 56px;
  }
  .bracket-base { stroke: var(--white); stroke-width: 7; fill: none; }
  .bracket-stitch { stroke: var(--cover-pink); stroke-width: 1.2; stroke-dasharray: 2 2; fill: none; }
  .flower-art {
    position: absolute;
    left: 240px;
    top: 356px;
    width: 134px;
    height: 154px;
    border-radius: 48% 52% 46% 54%;
    background: radial-gradient(circle at 50% 55%, #f6eef4 0%, #d9b4d6 45%, var(--soft-lilac) 75%, var(--ink-purple) 100%);
    box-shadow: 0 0 0 4px var(--white);
  }
</style>
</head>
<body>
<div class="canvas">
  <section class="book-cover">
    <svg class="cover-art" width="612" height="792" viewBox="0 0 612 792">
      <text class="author" x="306" y="72" text-anchor="middle" textLength="286" lengthAdjust="spacingAndGlyphs" transform="skewX(-6) translate(8 0)">Dra. Marta Quevedo Bonfanti Rocha</text>

      <path class="bracket-base" d="M221 510 V128 H404"/>
      <path class="bracket-stitch" d="M221 510 V128 H404"/>
      <path class="bracket-base" d="M412 348 V743 H233"/>
      <path class="bracket-stitch" d="M412 348 V743 H233"/>

      <text class="title-word" x="306" y="200" text-anchor="middle" textLength="46" lengthAdjust="spacingAndGlyphs">Nos</text>
      <text class="title-word" x="306" y="322" text-anchor="middle" textLength="118" lengthAdjust="spacingAndGlyphs">caminhos</text>
      <text class="title-word" x="306" y="583" text-anchor="middle" textLength="32" lengthAdjust="spacingAndGlyphs">do</text>
      <text class="title-word" x="306" y="705" text-anchor="middle" textLength="84" lengthAdjust="spacingAndGlyphs">berço</text>
    </svg>

    <div class="flower-art" role="img" aria-label="Ilustração de um lírio branco com manchas e estames roxos"></div>
  </section>
</div>
</body>
</html>
```